Flyer Design Project for The Verdance Studio

I'm a Naturopathic Herbalist who wishes to expand my business from x1 a week to x5 days a week and so need to produce a flyer to let people know what I do and to guide them to my website at theverdancestudio.com.au.
One-sided or double-sided A5 flyer on good quality paper for distribution by my referral network.  If all the info can fit on one side that would be great.
It would be great if the design could link up with my website i.e. the sun, mountains etc in the background but don't worry if not possible so then as an alternative I'd like to see something modern, fresh.
Otherwise it's to be simple, clean, easy to read, with a couple of relevant pictures if you want.

Target Market(s)
Predominantly females, from teens "clear skin tonics" to overloaded twenty-somethings, to pre-baby fertility programmes, healthy pregnancy etc
Industry/Entity Type
Business
Look and feel

```html
<!DOCTYPE html>
<html lang="en">
<head>
<meta charset="utf-8">
<title>The Verdance Studio – Herbal Medicine Flyer</title>
<link href="https://fonts.googleapis.com/css2?family=Quicksand:wght@400;500;600;700&display=swap" rel="stylesheet">
<style>
  :root {
    --backdrop: #e9e9e6;
    --green-light: #86c94a;
    --green-deep: #5fae2b;
    --green-text: #6cb52f;
    --white: #ffffff;
    --grey-text: #8a8a8a;
    --brand-purple: #8d5aa3;
    --herb-green: #7a9a5a;
    --cream: #eef0e6;
    --skin: #d9a27c;
  }
  * { box-sizing: border-box; margin: 0; padding: 0; }
  html, body { width: 1200px; height: 900px; overflow: hidden; }
  body {
    background: var(--backdrop);
    font-family: "Quicksand", sans-serif;
    position: relative;
  }
  .flyer-page {
    position: absolute;
    top: 58px;
    width: 545px;
    height: 784px;
    background: var(--white);
    overflow: hidden;
    box-shadow: 0 4px 14px rgba(0,0,0,0.18);
  }
  .flyer-front { left: 47px; }
  .flyer-back { left: 617px; width: 551px; }
  .page-wave { position: absolute; inset: 0; width: 100%; height: 100%; }

  /* Front */
  .front-question, .front-answer {
    position: absolute;
    left: 0; right: 0;
    text-align: center;
    color: var(--white);
    font-size: 31px;
    line-height: 39px;
    font-weight: 500;
  }
  .front-question { top: 103px; }
  .front-answer { top: 425px; }
  .front-question strong, .front-answer strong { font-weight: 700; }

  .photo-fill { position: absolute; }
  .herbs-mortar {
    left: 0; top: 610px; width: 135px; height: 140px;
    background: radial-gradient(ellipse at 55% 70%, var(--white) 0 38%, transparent 60%),
                linear-gradient(160deg, var(--herb-green), #b9c9a6 60%, var(--white));
    border-radius: 0 40px 0 0;
  }
  .skincare-bottles {
    left: 398px; top: 612px; width: 147px; height: 143px;
    background: linear-gradient(200deg, #7fbf4a 0%, #cfe6b4 35%, var(--cream) 60%, #f7f7f2 100%);
    border-radius: 40px 0 0 0;
  }
  .brand-name {
    position: absolute;
    left: 180px; width: 200px;
    top: 656px;
    text-align: center;
    color: var(--brand-purple);
    font-weight: 500;
    font-size: 21px;
    line-height: 24px;
  }
  .brand-dot {
    display: block;
    width: 22px; height: 22px;
    margin: 0 auto 8px;
    border-radius: 50%;
    background: var(--brand-purple);
  }

  /* Back */
  .portrait-frame {
    position: absolute;
    left: 29px; top: 51px;
    width: 161px; height: 151px;
    background: var(--white);
    padding: 7px;
    box-shadow: 3px 5px 8px rgba(0,0,0,0.3);
  }
  .portrait-photo {
    width: 100%; height: 100%;
    background: linear-gradient(135deg, #e6e6e6, #a9a9a9 55%, #7a7a7a);
  }
  .practitioner {
    position: absolute;
    left: 40px; top: 300px;
    width: 150px;
    color: var(--white);
  }
  .practitioner-name { font-size: 14.5px; font-weight: 700; line-height: 22px; }
  .practitioner-details { font-size: 11.5px; font-weight: 600; line-height: 20px; }

  .practice-copy {
    position: absolute;
    left: 212px; top: 53px;
    width: 331px;
    color: var(--white);
    font-size: 11.3px;
    line-height: 15.4px;
    font-weight: 600;
    text-align: justify;
  }
  .practice-copy p { margin-bottom: 15px; }

  .more-info {
    position: absolute;
    left: 44px; top: 636px;
    color: var(--grey-text);
    font-size: 13.5px;
    line-height: 18px;
  }
  .site-address {
    position: absolute;
    left: 44px; top: 720px;
    color: var(--green-text);
    font-weight: 700;
    font-size: 15.5px;
  }
  .seedling-hand {
    left: 277px; top: 640px; width: 274px; height: 126px;
    background: linear-gradient(180deg, rgba(255,255,255,0) 0%, #e8c4a4 45%, var(--skin) 70%, rgba(255,255,255,0) 100%);
    border-radius: 60px 0 0 60px;
  }
</style>
</head>
<body>

<section class="flyer-page flyer-front">
  <svg class="page-wave" viewBox="0 0 545 784" preserveAspectRatio="none" aria-hidden="true">
    <defs>
      <linearGradient id="frontGreen" x1="0" y1="0" x2="1" y2="1">
        <stop offset="0" stop-color="#86c94a"/>
        <stop offset="1" stop-color="#5fae2b"/>
      </linearGradient>
    </defs>
    <path d="M0 0 H545 V548 C430 598 260 625 0 560 Z" fill="url(#frontGreen)"/>
  </svg>

  <h1 class="front-question">
    <strong>Are you</strong> feeling tired,<br>
    run down,<br>
    under the weather<br>
    or simply just<br>
    <strong>feeling out of balance?</strong>
  </h1>

  <p class="front-answer">
    <strong>Herbal Medicine</strong><br>
    could be the answer<br>
    <strong>for you.</strong>
  </p>

  <div class="photo-fill herbs-mortar" role="img" aria-label="Fresh herbs in a white mortar and pestle"></div>
  <div class="brand-name"><span class="brand-dot"></span>The Verdance Studio</div>
  <div class="photo-fill skincare-bottles" role="img" aria-label="Natural skincare bottles with green leaves"></div>
</section>

<section class="flyer-page flyer-back">
  <svg class="page-wave" viewBox="0 0 551 784" preserveAspectRatio="none" aria-hidden="true">
    <defs>
      <linearGradient id="backGreen" x1="0" y1="0" x2="1" y2="1">
        <stop offset="0" stop-color="#86c94a"/>
        <stop offset="1" stop-color="#5fae2b"/>
      </linearGradient>
    </defs>
    <path d="M0 0 H551 V575 C430 622 260 632 0 588 Z" fill="url(#backGreen)"/>
  </svg>

  <div class="portrait-frame">
    <div class="portrait-photo" role="img" aria-label="Portrait photo of the herbalist"></div>
  </div>

  <div class="practitioner">
    <p class="practitioner-name">Maren Holt DHM,</p>
    <p class="practitioner-details">
      Local Naturopathic<br>
      Herbalist joins the<br>
      professional team at<br>
      Willow and Fern Clinic<br>
      48 Banksia Street,<br>
      Coogee, NSW,<br>
      2034 0412 555 018
    </p>
  </div>

  <div class="practice-copy">
    <p>Maren has a wealth of experience with over 14 years in clinical practice which, coupled with a great deal of “life experience” as the mother of three children, helps to make your consultation professional, caring and healing.</p>
    <p>Passionate about helping you reach your highest potential health-wise, Maren will make you a “Daily Wellness Tonic” which is like the best multi-vitamin you could have as it’s tailor-made especially for you. The “Daily Wellness Tonic” can help strengthen, nourish, heal and rebalance your whole body.</p>
    <p>“Daily Wellness Tonics” can be made to assist you keeping yourself well, for nurturing yourself (so in turn you can nurture others), for re-energising you, for aging gracefully, to assist you feeling back on top of life and to help you face challenges more easily.</p>
    <p>Herbal medicine can help with Sleep Disorders, Weak Immune Systems, Anxiety, Depression, Fertility issues, Childhood Diseases, Skin Problems, Gastro-Intestinal Disorders and Women’s Health.</p>
    <p>Maren also specialises in “Super Immune Boost Tonics” assisting with acute conditions such as coughs, colds, sore throats and offers 20-30 minute “Express Appointments”. Useful as a preventative measure or as a way of healing these conditions more quickly.</p>
    <p>“Clear Skin Wellness Tonics” are popular with teens and a special teen package is also offered as an “Express Appointment” with a bottle of tonic.</p>
  </div>

  <p class="more-info">For more information,<br>check out The Verdance Studio<br>website at</p>
  <p class="site-address">www.theverdancestudio.com.au</p>
  <div class="photo-fill seedling-hand" role="img" aria-label="Open hand holding soil with a small green seedling"></div>
</section>

</body>
</html>
```